Flyers

Modify Existing Flyer and create another for exterior company
Updates

Previous Brief has been updated- we want to update this existing one also

Target Market(s)

Exterior Remodeling Customers

Industry/Entity Type

Remodeling/Construction

```html
<!DOCTYPE html>
<html lang="en">
<head>
<meta charset="utf-8">
<title>Halden Roofing and Exteriors – Remodeling Flyer</title>
<link rel="stylesheet" href="https://fonts.googleapis.com/css2?family=Fira+Sans:wght@600;700;800&family=Hind:wght@400;500&display=swap">
<style>
  :root{
    --orange:#f15a24;
    --blue:#0b72c9;
    --black:#050505;
    --white:#ffffff;
    --ink:#2b2b2b;
    --page:#dcdcdc;
  }
  *{box-sizing:border-box;margin:0;padding:0}
  html,body{width:1200px;height:1200px;overflow:hidden}
  body{background:var(--page);position:relative;font-family:"Hind",sans-serif;color:var(--ink)}
  .flyer{position:absolute;left:150px;top:17px;width:900px;height:1165px;background:var(--white);overflow:hidden}
  .layer{position:absolute;left:0;top:0}
  .headline{position:absolute;left:51px;top:22px;font-family:"Fira Sans",sans-serif;font-weight:700;font-size:31px;line-height:43px;color:var(--white)}
  .brand{position:absolute;left:545px;top:0;width:355px;height:176px;display:flex;align-items:center;justify-content:center;gap:12px;color:var(--white);font-family:"Fira Sans",sans-serif;font-weight:700}
  .brand-mark{width:22px;height:22px;background:var(--orange);flex:none}
  .brand-name{font-size:24px;line-height:1.15;text-transform:uppercase;letter-spacing:.5px}
  .tagline{position:absolute;left:51px;top:508px;font-family:"Fira Sans",sans-serif;font-weight:800;font-size:27px;line-height:37px;color:var(--white);text-transform:uppercase}
  .service{position:absolute}
  .service h2{font-family:"Fira Sans",sans-serif;font-weight:700;font-size:19px;line-height:22px;color:var(--orange);text-transform:uppercase}
  .service p{font-size:13.6px;line-height:17.7px;margin-top:1px}
  .service p.justify{text-align:justify}
  .ticks{list-style:none;margin-top:3px}
  .ticks li{position:relative;padding-left:16px;font-size:13.6px;line-height:20.6px}
  .ticks li.wrap{line-height:17.7px;padding-top:2px;padding-bottom:1px}
  .ticks li::before{content:"";position:absolute;left:0;top:6px;width:9px;height:9px;border-radius:50%;background:var(--blue)}
  .ticks li::after{content:"";position:absolute;left:2.5px;top:8px;width:3px;height:4.5px;border:solid var(--white);border-width:0 1.4px 1.4px 0;transform:rotate(40deg)}
  .icon{position:absolute;width:46px;height:46px}
  .photo{position:absolute}
  .kitchen-photo{left:292px;top:750px;width:140px;height:106px;background:linear-gradient(160deg,#f1efe9,#c9c4ba 55%,#6b4a33)}
  .bath-photo{left:292px;top:967px;width:140px;height:119px;background:linear-gradient(150deg,#dfe6ea,#b9c3c9 55%,#eef0f0)}
  .bedroom-photo{left:697px;top:733px;width:165px;height:123px;background:linear-gradient(170deg,#e9ecee,#c9cdd0 60%,#8d8a86)}
  .deck-photo{float:right;clear:right;width:148px;height:109px;margin:4px 0 0 8px;background:linear-gradient(180deg,#a4794c,#7fae5f 45%,#5a3a28)}
  .float-spacer{float:right;width:0;height:53px}
  .footer-text{position:absolute;left:51px;top:1106px;font-family:"Fira Sans",sans-serif;color:var(--white);font-size:18px;line-height:24px;text-transform:uppercase;font-weight:600}
  .footer-text strong{font-weight:700}
  .footer-text .phone{display:inline-flex;align-items:center;gap:4px;font-weight:600}
  .web{position:absolute;left:546px;top:1117px;display:flex;align-items:center;gap:10px;font-family:"Fira Sans",sans-serif;font-weight:600;font-size:20px;color:var(--white)}
</style>
</head>
<body>
<div class="flyer">
  <svg class="layer" width="900" height="1165" viewBox="0 0 900 1165" aria-hidden="true">
    <defs>
      <linearGradient id="kitchenTone" x1="0" y1="0" x2="1" y2="1">
        <stop offset="0" stop-color="#f6f3ec"/><stop offset=".6" stop-color="#e6dccb"/><stop offset="1" stop-color="#a88a66"/>
      </linearGradient>
      <linearGradient id="bathTone" x1="0" y1="0" x2="1" y2="1">
        <stop offset="0" stop-color="#c7d0d6"/><stop offset=".5" stop-color="#e6e6e3"/><stop offset="1" stop-color="#d8d4cf"/>
      </linearGradient>
    </defs>
    <polygon points="0,0 487,0 534,176 0,176" fill="var(--orange)"/>
    <polygon points="487,0 900,0 900,176 534,176" fill="var(--black)"/>
    <polygon points="0,183 407,183 477,495 0,495" fill="url(#kitchenTone)" role="img" aria-label="Photo of a bright white remodeled kitchen with island and pendant lights"/>
    <polygon points="413,183 900,183 900,600 500,600" fill="url(#bathTone)" role="img" aria-label="Photo of a remodeled bathroom with glass tile shower and marble vanity"/>
    <polygon points="0,495 601,495 636,600 0,600" fill="var(--white)"/>
    <polygon points="0,500 596,500 628,600 0,600" fill="var(--blue)"/>
    <polygon points="0,1096 451,1096 474,1165 0,1165" fill="var(--blue)"/>
    <polygon points="458,1096 900,1096 900,1165 481,1165" fill="var(--orange)"/>
  </svg>

  <h1 class="headline">Ready for<br>a Beautiful and Functional<br>Kitchen or Bathroom?</h1>

  <div class="brand"><span class="brand-mark"></span><span class="brand-name">Halden<br>Roofing and Exteriors</span></div>

  <p class="tagline">Work with a top-rated local<br>remodeling company in Ankeny, IA</p>

  <!-- Kitchen remodeling -->
  <svg class="icon" style="left:36px;top:622px" viewBox="0 0 46 46" fill="none" stroke-width="1.6" aria-hidden="true">
    <path d="M4 10h10M6 10l2-6h2l2 6M20 6v8M26 4v10" stroke="var(--orange)"/>
    <rect x="3" y="24" width="26" height="18" stroke="var(--blue)"/>
    <path d="M3 30h26M16 30v12M7 34h6" stroke="var(--blue)"/>
    <rect x="32" y="16" width="10" height="26" stroke="var(--blue)"/>
    <path d="M32 26h10" stroke="var(--blue)"/>
  </svg>
  <div class="service" style="left:95px;top:619px;width:337px">
    <h2>Kitchen Remodeling</h2>
    <p>Whatever your vision is for your new kitchen, our crew can help you bring it to life. You can trust us for:</p>
    <ul class="ticks">
      <li>Open concept design services</li>
      <li>Kitchen cabinet installation services</li>
      <li>Kitchen countertop installation services</li>
      <li>Tile installation services</li>
      <li>Lighting installation services</li>
      <li>Plumbing upgrade services</li>
      <li>Electrical upgrade services</li>
      <li>Drywall services</li>
      <li>Painting services</li>
    </ul>
  </div>
  <div class="photo kitchen-photo" role="img" aria-label="Photo of a white kitchen with marble island and wood floor"></div>

  <!-- Home additions -->
  <svg class="icon" style="left:473px;top:622px" viewBox="0 0 46 46" fill="none" stroke-width="1.6" aria-hidden="true">
    <path d="M3 20L23 5l20 15" stroke="var(--orange)"/>
    <path d="M7 18v24h32V18" stroke="var(--blue)"/>
    <rect x="12" y="26" width="7" height="7" stroke="var(--blue)"/>
    <rect x="27" y="26" width="7" height="16" stroke="var(--blue)"/>
    <path d="M3 42h40" stroke="var(--blue)"/>
  </svg>
  <div class="service" style="left:538px;top:619px;width:324px">
    <h2>Home Additions</h2>
    <p class="justify">No matter what kind of space you need, our team will bring your vision to life. You can hire us if you need a:</p>
    <ul class="ticks">
      <li>Bathroom addition</li>
      <li>Bedroom addition</li>
      <li>Garage addition</li>
      <li>Basement addition</li>
      <li>Guest room addition</li>
      <li>Living room addition</li>
      <li>Sunroom addition</li>
    </ul>
  </div>
  <div class="photo bedroom-photo" role="img" aria-label="Photo of a bright bedroom addition with large windows"></div>

  <!-- Bathroom remodeling -->
  <svg class="icon" style="left:36px;top:888px" viewBox="0 0 46 46" fill="none" stroke-width="1.6" aria-hidden="true">
    <rect x="24" y="3" width="18" height="12" stroke="var(--orange)"/>
    <path d="M4 16h10v10H4zM4 26c0 6 4 9 9 9v7M22 22h20v8c0 4-3 6-6 6h-8c-3 0-6-2-6-6z" stroke="var(--blue)"/>
    <path d="M32 36v6M26 42h12" stroke="var(--blue)"/>
  </svg>
  <div class="service" style="left:95px;top:885px;width:337px">
    <h2>Bathroom Remodeling</h2>
    <p class="justify">When you hire us for your bathroom remodeling project, the possibilities are endless. Our experienced and talented team can:</p>
    <ul class="ticks" style="width:165px">
      <li class="wrap">Install a custom tile shower</li>
      <li>Build a new vanity</li>
      <li>Install flooring and tile</li>
      <li class="wrap">Replace your plumbing and light fixtures</li>
    </ul>
  </div>
  <div class="photo bath-photo" role="img" aria-label="Photo of a bathroom with glass shower and freestanding tub"></div>

  <!-- Decks / patios -->
  <svg class="icon" style="left:473px;top:888px" viewBox="0 0 46 46" fill="none" stroke-width="1.6" aria-hidden="true">
    <path d="M8 16a15 12 0 0 1 30 0z" stroke="var(--orange)"/>
    <path d="M23 16v20" stroke="var(--orange)"/>
    <path d="M5 30h36M10 30l-4 12M36 30l4 12M4 42h38" stroke="var(--blue)"/>
  </svg>
  <div class="service" style="left:538px;top:887px;width:324px">
    <h2>Decks/Patios</h2>
    <p class="justify"><span class="float-spacer"></span><span class="photo deck-photo" style="position:static;display:block" role="img" aria-label="Photo of a covered wooden deck with dining table"></span>An outdoor space is a great addition to any residential property. When you decide to build a patio or deck, you’ll be able to experience a variety of benefits. Your outdoor area will increase your:</p>
    <ul class="ticks">
      <li>Property value</li>
      <li>Curb appeal</li>
      <li>Functional living</li>
      <li>Space</li>
    </ul>
  </div>

  <p class="footer-text">Call today for your<br><strong>Free estimate</strong>
    <span class="phone"><svg width="16" height="16" viewBox="0 0 16 16" aria-hidden="true"><circle cx="8" cy="8" r="8" fill="var(--white)"/><path d="M5 4l2 0 .6 2-1 .8c.5 1 1.3 1.8 2.4 2.4l.8-1 2 .6v2c-3.5.3-7-3.2-6.8-6.8z" fill="var(--blue)"/></svg>555-014-2260</span>
  </p>

  <div class="web">
    <svg width="22" height="22" viewBox="0 0 22 22" fill="none" stroke="var(--white)" stroke-width="1.4" aria-hidden="true">
      <circle cx="11" cy="11" r="9"/><ellipse cx="11" cy="11" rx="4" ry="9"/><path d="M2 11h18M4 6h14M4 16h14"/>
    </svg>
    <span>www.haldenexteriors.com</span>
  </div>
</div>
</body>
</html>
```